website for 'thebrightnook' which is a specialise tutoring company for children with learning difficu

We need a website for a new business that is focused on assessment and then specialised tutoring for young children with learning difficulties. The website needs to be simple but fun and fresh. We have an existing logo (uploaded) that needs to be the building block for the website. The website doesn't need to be overly content-heavy.

Target Market(s)

parents

Industry/Entity Type

Education

Number of Pages Required

3 page

Font styles to use
Other font styles liked:
• possibly matched to the logo

Requirements
Must have
• a initial front page which introduces the business and provides contact details, a second page that will allow for a more content-heavy section, a third page which focuses on introducing the staff (initially 3 staff ),

```html
<!DOCTYPE html>
<html lang="en">
<head>
<meta charset="utf-8">
<title>The Bright Nook – Specialised Tutoring</title>
<link rel="stylesheet" href="https://fonts.googleapis.com/css2?family=Crimson+Pro:wght@400;500;600&display=swap">
<style>
:root{
  --green-deep:#3f6f1c;
  --green:#5a8f2a;
  --green-mid:#6a9f34;
  --green-light:#8dc63f;
  --green-pale:#a6cc52;
  --yellow:#f7e46a;
  --ink:#1a1a1a;
  --text:#555;
  --white:#fff;
  --black:#0c0c0c;
}
*{margin:0;padding:0;box-sizing:border-box}
html,body{width:1081px;height:1200px;overflow:hidden}
body{position:relative;font-family:"Crimson Pro",Georgia,serif;background:var(--green-light);color:var(--ink)}
.abs{position:absolute}

.top-line{left:0;top:0;width:1081px;height:4px;background:var(--yellow);z-index:3}
.hero{left:0;top:0;width:1081px;height:576px;
  background:linear-gradient(100deg,#8a6a55 0%,#c99c7a 22%,#6f83a6 45%,#c9b7b0 62%,#d4467a 75%,#3a74c8 88%,#b9a78d 100%);}
.call-tab{left:485px;top:4px;width:205px;height:24px;background:#2a1c1c;color:var(--white);
  font-size:17px;line-height:24px;text-align:center;border-radius:10px 0 0 0}
.consult-tab{left:690px;top:4px;width:320px;height:29px;background:var(--yellow);color:var(--ink);
  font-size:13.5px;line-height:27px;padding-left:25px;border-radius:0 0 16px 0}

.brand-box{left:67px;top:4px;width:218px;height:160px}
.brand-name{left:67px;top:76px;width:218px;text-align:center;font-size:30px;font-weight:500;color:var(--green);letter-spacing:-0.5px}
.brand-dot{left:160px;top:28px;width:32px;height:32px;border-radius:50%;background:var(--green-mid)}
.brand-tag{left:67px;top:117px;width:218px;text-align:center;font-size:10.5px;letter-spacing:1.6px;color:#666}

.banner{left:449px;top:327px;width:566px;height:90px}
.banner-text{left:476px;top:333px;color:var(--white)}
.banner-title{font-size:40px;line-height:44px;font-weight:500}
.banner-sub{font-size:27px;line-height:30px}

.green-field{left:0;top:576px;width:1081px;height:405px;
  background:linear-gradient(180deg,var(--green) 0%,#73ad35 55%,var(--green-light) 100%);border-top:4px solid var(--green-deep)}

.nav{left:67px;top:552px;width:948px;height:47px;background:var(--white)}
.nav ul{position:absolute;left:0;top:10px;width:948px;height:37px;background:var(--black);list-style:none;display:flex;
  border-top:1px solid #444;border-bottom:2px solid #333}
.nav li{color:var(--white);font-size:16px;line-height:34px;padding:0 12px;border-right:1px solid #555}
.nav li:last-child{border-right:0}

.panel{left:67px;top:599px;width:948px;height:343px;background:linear-gradient(180deg,#fbfbfb 0%,#e7e7e7 100%);
  box-shadow:0 8px 10px -4px rgba(0,0,0,.45)}
.welcome-title{left:92px;top:628px;font-size:27px;font-weight:400;color:var(--ink)}
.welcome-rule{left:92px;top:669px;width:598px;height:3px;border-top:1px solid #c8c8c8;border-bottom:1px solid #c8c8c8}
.welcome-copy{left:92px;top:682px;width:604px;font-size:13.4px;line-height:21.6px;color:var(--text)}
.read-more{left:94px;top:867px;width:98px;height:31px;background:var(--yellow);border:1px solid #e2cf4f;border-radius:3px;
  font-size:13px;line-height:29px;text-align:center;color:#333}

.contact-card{left:715px;top:625px;width:274px;height:293px;border-radius:8px;
  background:linear-gradient(160deg,#66a030 0%,#558c27 50%,#3f6f1c 100%);border:1px solid #3a661a;color:var(--white);
  box-shadow:0 2px 4px rgba(0,0,0,.3)}
.contact-card h2{position:absolute;left:25px;top:20px;font-size:26px;font-weight:400}
.contact-card .rule{position:absolute;left:25px;width:224px;border-top:1px solid rgba(255,255,255,.25)}
.contact-row{position:absolute;left:25px;width:230px;display:flex;gap:10px;font-size:13.5px;line-height:19px}
.contact-row svg{flex:none;margin-top:0}

.footer{left:0;top:981px;width:1081px;height:186px;background:var(--green)}
.footer-brand{left:83px;top:1058px;font-size:28px;font-weight:500;color:var(--white);letter-spacing:-0.5px}
.footer-dot{left:170px;top:1012px;width:32px;height:32px;border-radius:50%;background:var(--green-light)}
.footer-tag{left:83px;top:1100px;width:190px;font-size:10px;letter-spacing:1.5px;color:#e6f1d6}
.f-col{top:1004px;color:#e8f3da}
.f-col h3{font-size:13.5px;font-weight:400;color:var(--white);margin-bottom:9px;letter-spacing:.2px}
.f-col p{font-size:12px;line-height:16.6px}
.social{display:flex;gap:6px;margin-top:4px}
.social span{width:22px;height:22px;border-radius:50%;border:1.5px solid var(--white)}
.news-input{left:788px;top:1058px;width:226px;height:25px;background:var(--white);font-size:12px;line-height:25px;padding-left:8px;color:#555}
.news-btn{left:788px;top:1092px;width:67px;height:25px;background:var(--green-pale);font-size:12.5px;line-height:25px;text-align:center;color:#2d4d12}

.copyright{left:0;top:1167px;width:1081px;height:33px;background:var(--green-pale);text-align:center;font-size:12px;line-height:33px;color:#3c5a1c}
</style>
</head>
<body>
<div class="abs hero" role="img" aria-label="Photo of a tutor helping a young girl at a desk in a bright classroom"></div>
<div class="abs top-line"></div>
<div class="abs call-tab">Call Us: 1800 555 0142</div>
<div class="abs consult-tab">CONTACT US FOR A FREE CONSULTATION</div>

<svg class="abs brand-box" viewBox="0 0 218 160" aria-hidden="true">
  <polygon points="0,0 218,0 218,148 109,160 0,148" fill="#fff"/>
</svg>
<div class="abs brand-dot"></div>
<div class="abs brand-name">thebrightnook</div>
<div class="abs brand-tag">specialised learning for children</div>

<svg class="abs banner" viewBox="0 0 566 90" aria-hidden="true">
  <polygon points="14,0 566,0 548,90 0,90" fill="#5f9a2c" opacity=".93"/>
</svg>
<div class="abs banner-text">
  <div class="banner-title">Specialised Tutoring</div>
  <div class="banner-sub">For Young Children With Learning Difficulties</div>
</div>

<div class="abs green-field"></div>

<nav class="abs nav">
  <ul>
    <li>HOME</li><li>ABOUT US</li><li>TUTORING PROGRAMS</li><li style="padding:0 16px">YOUNG LEARNERS</li><li style="padding:0 14px">OUR TUTORS</li><li style="padding:0 14px">CONTACT US</li><li style="padding:0 13px">GET STARTED</li>
  </ul>
</nav>

<div class="abs panel"></div>
<h1 class="abs welcome-title">Welcome to The Bright Nook</h1>
<div class="abs welcome-rule"></div>
<p class="abs welcome-copy">Lorem ipsum dolor sit amet, consectetur adipiscing elit, sed do eiusmod tempor incididunt ut labore et dolore magna aliqua. Ut enim ad minim veniam, quis nostrud exercitation ullamco laboris nisi ut aliquip ex ea commodo consequat. Duis aute irure dolor in reprehenderit in voluptate velit esse cillum dolore eu fugiat nulla pariatur. Excepteur sint occaecat cupidatat non proident, sunt in culpa qui officia deserunt mollit anim id est laborum. quis nostrud exercitation ullamco laboris nisi ut aliquip ex ea commodo consequat. Duis aute irure dolor in reprehenderit in voluptate velit esse cillum dolore eu fugiat nulla pariatur. Excepteur sint occaecat cupidatat non proident, sunt in culpa qui officia deserunt mollit anim id est laborum.</p>
<div class="abs read-more">READ MORE</div>

<section class="abs contact-card">
  <h2>Contact Us</h2>
  <div class="rule" style="top:61px"></div>
  <div class="contact-row" style="top:80px">
    <svg width="26" height="26" viewBox="0 0 26 26"><circle cx="13" cy="13" r="11.5" fill="none" stroke="#f7e46a" stroke-width="1.8"/><path d="M13 6.5a4 4 0 0 0-4 4c0 3 4 8 4 8s4-5 4-8a4 4 0 0 0-4-4z" fill="none" stroke="#f7e46a" stroke-width="1.6"/><circle cx="13" cy="10.5" r="1.3" fill="#f7e46a"/></svg>
    <div>Your Company LTD.<br>Street Name, 000000<br>City Name</div>
  </div>
  <div class="rule" style="top:144px"></div>
  <div class="contact-row" style="top:159px">
    <svg width="26" height="26" viewBox="0 0 26 26"><circle cx="13" cy="13" r="11.5" fill="none" stroke="#f7e46a" stroke-width="1.8"/><path d="M9 7.5l2.3 2.5-1.3 1.8c.8 1.7 2 2.9 3.7 3.7l1.8-1.3 2.5 2.3-1.6 1.8c-4.5-.6-8.5-4.6-9.1-9.1z" fill="none" stroke="#f7e46a" stroke-width="1.5" stroke-linejoin="round"/></svg>
    <div>Phone<br>1800 555 0142</div>
  </div>
  <div class="rule" style="top:202px"></div>
  <div class="contact-row" style="top:217px">
    <svg width="26" height="26" viewBox="0 0 26 26"><circle cx="13" cy="13" r="11.5" fill="none" stroke="#f7e46a" stroke-width="1.8"/><path d="M7.5 11.5l5.5-4 5.5 4v6h-11z M7.5 11.5l5.5 4 5.5-4" fill="none" stroke="#f7e46a" stroke-width="1.5" stroke-linejoin="round"/></svg>
    <div>Email<br>hello@brightnook.example</div>
  </div>
</section>

<footer class="abs footer"></footer>
<div class="abs footer-dot"></div>
<div class="abs footer-brand">thebrightnook</div>
<div class="abs footer-tag">specialised learning for children</div>

<div class="abs f-col" style="left:302px">
  <h3>QUICK LINKS</h3>
  <p>Home<br>About Us<br>Tutoring Programs<br>Young Learners<br>Our Tutors<br>Contact Us<br>Get Started</p>
</div>
<div class="abs f-col" style="left:420px">
  <h3>CONTACT US</h3>
  <p>Your Company LTD.<br>Street Name, 000000<br>City Name<br><br>T: 1800 555 0142<br>hello@brightnook.example</p>
</div>
<div class="abs f-col" style="left:560px">
  <h3>COMPANY</h3>
  <p>Privacy Policy<br>Terms &amp; Conditions</p>
</div>
<div class="abs f-col" style="left:689px">
  <h3>FOLLOW US</h3>
  <div class="social"><span></span><span></span></div>
</div>
<div class="abs f-col" style="left:788px">
  <h3>SUBSCRIBE TO OUR NEWSLETTER</h3>
  <p>Get the Best Deals First</p>
</div>
<div class="abs news-input">Enter Your E-mail</div>
<div class="abs news-btn">SUBSCRIBE</div>

<div class="abs copyright">© 2016 THE BRIGHT NOOK. ALL RIGHTS RESERVED</div>
</body>
</html>
```